Motivation health and wellbeing counselling. 'Open Meadow Now' Open Meadow for Spring' Open Meadow Path'

I need a design for my a new buisness aimed at women in the middle age range. Motivational coaching and counselling for weight loss, depression and anxiety and other mental health conditions, addiction, loss of confidence, menopause, empty nest syndrome and other life changing events. Experienced qualified counsellor with a lived experience to provide 1:1 counselling as well as the option for group sessions and social media online support. Long term sustainable change goals to support persistant progress in exercise, healthy eating and positive lifestyle changes. The card should promote a somewhat funky feminine positive message. I would like to trial the colours magenta, red, yellow and a bold blue or green.

Mental Health

```html
<!DOCTYPE html>
<html lang="en">
<head>
<meta charset="utf-8">
<title>Open Meadow for Spring – Business Card</title>
<link rel="stylesheet" href="https://fonts.googleapis.com/css2?family=Open+Sans:wght@400;600&display=swap">
<style>
  :root {
    --backdrop: #d9d9d9;
    --card-amber: #f7b52c;
    --card-gold: #fbd36a;
    --card-cream: #fff6dc;
    --magenta: #c8308c;
    --red: #e8274b;
    --blue: #2f5fc4;
    --sky: #4a8ad6;
    --ink-blue: #1f3a94;
    --ornament: #fbe2a0;
    --wave-light: #fbc64a;
    --wave-deep: #f9b832;
    --wave-cream: #fff1c8;
  }
  * { box-sizing: border-box; margin: 0; padding: 0; }
  html, body {
    width: 1200px; height: 900px; overflow: hidden;
    background: var(--backdrop);
    font-family: "Open Sans", sans-serif;
  }
  .business-card {
    position: absolute; left: 100px; top: 150px;
    width: 1000px; height: 600px;
    border-radius: 40px; overflow: hidden;
    background: linear-gradient(100deg, var(--card-amber) 0%, var(--card-gold) 45%, var(--card-cream) 100%);
  }
  .floral-decoration {
    position: absolute; left: 430px; top: 60px;
    width: 560px; height: 440px;
    border-radius: 50%;
    background: radial-gradient(ellipse at center, var(--ornament) 0%, rgba(251,226,160,0) 70%);
    opacity: .8;
  }
  .brand-mark {
    position: absolute; left: 70px; top: 70px;
    width: 170px; height: 170px; border-radius: 50%;
    background: var(--magenta);
  }
  .brand-name {
    position: absolute; left: 285px; top: 110px;
    font-size: 58px; font-weight: 400; color: var(--magenta);
    letter-spacing: -0.5px; white-space: nowrap;
  }
  .brand-tagline {
    position: absolute; left: 290px; top: 192px;
    font-size: 24px; color: var(--sky); white-space: nowrap;
  }
  .social-links {
    position: absolute; left: 788px; top: 322px;
    display: flex; gap: 6px;
  }
  .social-links span {
    width: 28px; height: 28px; border-radius: 5px; background: var(--sky);
  }
  .contact-list {
    position: absolute; left: 60px; top: 325px;
    list-style: none; color: var(--ink-blue);
    font-size: 24px; line-height: 34px;
    z-index: 2;
  }
  .contact-list li { display: flex; align-items: center; gap: 6px; white-space: nowrap; }
  .contact-list svg { width: 26px; height: 26px; flex: none; fill: var(--magenta); }
  .contact-list .continued { padding-left: 32px; }
  .swooshes { position: absolute; left: 0; top: 0; }
</style>
</head>
<body>
  <main class="business-card">
    <div class="floral-decoration" role="img" aria-label="Soft pale floral flourish decoration"></div>

    <svg class="swooshes" width="1000" height="600" viewBox="0 0 1000 600" aria-hidden="true">
      <path d="M0 548 C 250 525, 520 595, 1000 455 L1000 600 L0 600 Z" fill="var(--wave-light)"/>
      <path d="M0 578 C 300 555, 600 605, 1000 520 L1000 600 L0 600 Z" fill="var(--wave-deep)"/>
      <path d="M0 512 C 250 495, 450 525, 620 522 C 780 518, 880 420, 1000 380 L1000 391 C 880 432, 780 530, 620 532 C 450 534, 250 508, 0 522 Z" fill="var(--wave-cream)"/>
      <path d="M0 526 C 250 506, 450 540, 620 536 C 780 532, 880 432, 1000 396 L1000 410 C 880 450, 780 550, 620 552 C 450 556, 250 530, 0 548 Z" fill="var(--red)"/>
      <path d="M420 542 C 640 534, 880 452, 988 288 C 940 470, 690 560, 420 542 Z" fill="var(--blue)"/>
      <path d="M380 566 C 470 570, 560 574, 650 570 C 560 582, 470 580, 380 566 Z" fill="var(--blue)"/>
    </svg>

    <div class="brand-mark" role="img" aria-label="Open Meadow for Spring brand mark"></div>
    <h1 class="brand-name">Open Meadow for Spring</h1>
    <p class="brand-tagline">Motivation health and wellbeing counselling</p>

    <div class="social-links" aria-label="Social media links"><span></span><span></span></div>

    <ul class="contact-list">
      <li><svg viewBox="0 0 24 24"><path d="M6.6 10.8a15 15 0 0 0 6.6 6.6l2.2-2.2a1 1 0 0 1 1-.25 11.4 11.4 0 0 0 3.6.6 1 1 0 0 1 1 1V20a1 1 0 0 1-1 1A17 17 0 0 1 3 4a1 1 0 0 1 1-1h3.5a1 1 0 0 1 1 1c0 1.25.2 2.45.6 3.6a1 1 0 0 1-.25 1z"/></svg>(555) 318-2094</li>
      <li><svg viewBox="0 0 24 24"><path d="M3 5h18v14H3z M3 5l9 7 9-7" stroke="#fff" stroke-width="1.5"/></svg>hello@openmeadowspring.com</li>
      <li><svg viewBox="0 0 24 24"><circle cx="12" cy="12" r="9"/><path d="M3 12h18M12 3c3 3 3 15 0 18M12 3c-3 3-3 15 0 18" stroke="#fff" stroke-width="1.3" fill="none"/></svg>www.openmeadowspring.com</li>
      <li><svg viewBox="0 0 24 24"><path d="M12 3 2 12h3v9h5v-6h4v6h5v-9h3z"/></svg>Suite 12, 48 Larkfield Lane</li>
      <li class="continued">Brookvale, Ohio 45012</li>
    </ul>
  </main>
</body>
</html>
```